Veltrano Business Card

I have a business that is called "Brevant Electrical Products LTD" My company deals with top of the range laptops and mobile phones that are exclusive. I need a business card that will be eye catching but not over complicated.

Target Market(s)

Adults aged 19 to 50
Upper middle class

Industry/Entity Type

Business

Requirements
Must have
• Company name/logo (file attached)
• It must have my contact information which is:

• Name: Dale Marwick

• Position: Managing Director 

• Business Address: 7 Hapton Row, London, W4 9QD

• Contact Number: 02085193604
• Mobile: 07814260537
• Email: info@veltrano-goods.co.uk
Nice to have
• Simple and stylish
• Eye catching

```html
<!DOCTYPE html>
<html lang="en">
<head>
<meta charset="utf-8">
<title>Veltrano Business Card</title>
<link href="https://fonts.googleapis.com/css2?family=Questrial&display=swap" rel="stylesheet">
<style>
  :root {
    --paper: #ffffff;
    --ink: #3b5478;
    --brand: #1f8fbf;
    --sky-top: #ffffff;
    --sky-bottom: #5ec9ea;
    --trim: #111111;
  }
  html, body {
    margin: 0;
    padding: 0;
    overflow: hidden;
    background: var(--paper);
  }
  .card {
    position: relative;
    width: 1200px;
    height: 799px;
    background: var(--paper);
    overflow: hidden;
    font-family: "Questrial", "Century Gothic", sans-serif;
    color: var(--ink);
  }
  .sky-band {
    position: absolute;
    left: 27px;
    top: 480px;
    width: 1145px;
    height: 291px;
    background: linear-gradient(to bottom, var(--sky-top) 0%, var(--sky-bottom) 100%);
  }
  .trim-marks {
    position: absolute;
    inset: 0;
  }
  .brand {
    position: absolute;
    left: 144px;
    top: 140px;
    margin: 0;
    font-weight: 400;
    color: var(--brand);
  }
  .brand-name {
    display: block;
    font-size: 78px;
    line-height: 92px;
    letter-spacing: 2px;
  }
  .brand-line {
    display: block;
    font-size: 33px;
    line-height: 40px;
    letter-spacing: 2.5px;
    margin-left: 3px;
  }
  .person {
    position: absolute;
    left: 146px;
    top: 434px;
    font-size: 34px;
    line-height: 39px;
  }
  .person p { margin: 0; }
  .contact {
    position: absolute;
    right: 148px;
    top: 430px;
    text-align: right;
    font-size: 31px;
    line-height: 48.5px;
    margin: 0;
    font-style: normal;
  }
  .contact p { margin: 0; }
</style>
</head>
<body>
  <main class="card">
    <div class="sky-band"></div>

    <svg class="trim-marks" width="1200" height="799" viewBox="0 0 1200 799" aria-hidden="true">
      <g stroke="var(--trim)" stroke-width="1">
        <line x1="85.5" y1="0" x2="85.5" y2="60"/>
        <line x1="1115.5" y1="0" x2="1115.5" y2="60"/>
        <line x1="0" y1="84.5" x2="60" y2="84.5"/>
        <line x1="1140" y1="84.5" x2="1200" y2="84.5"/>
        <line x1="0" y1="715.5" x2="60" y2="715.5"/>
        <line x1="1140" y1="715.5" x2="1200" y2="715.5"/>
        <line x1="85.5" y1="739" x2="85.5" y2="799"/>
        <line x1="1115.5" y1="739" x2="1115.5" y2="799"/>
      </g>
    </svg>

    <h1 class="brand">
      <span class="brand-name">VELTRANO</span>
      <span class="brand-line">Electrical Products</span>
    </h1>

    <section class="person">
      <p class="person-name">Dale Marwick</p>
      <p class="person-role">Managing Director</p>
    </section>

    <address class="contact">
      <p>7 Hapton Row,</p>
      <p>London, W4 9QD</p>
      <p>p: 02085193604</p>
      <p>m: 07814260537</p>
      <p>e: info@veltrano-goods.co.uk</p>
    </address>
  </main>
</body>
</html>
```